Business cards for start-up accounting firm

I'm looking for a double sided business card ready for upload into Lumo print or similar print providers with no modification required by me.
I'm looking for something simple as i think cards that are too 'busy' actually detract from the message. I have some thoughts but more than happy to see what comes up. The logo i have came out of left field and i love it the moment i saw it!

My thoughts:

Side 1: Just the logo, perhaps on a dark grey or charcoal background to make the logo colours stand out?

Side 2: The call to action from me website 'Looking for a more relaxed, friendly and interactive relationship with your accountant?' with my contact information
Name: Gus Tarrow
Email: gus@ledgerowl.com.au
Website: www.ledgerowl.com.au
Phone: 1300 762 349

The call to action needs to be the first thing they see when they look at side 2. If it helps to know what we do and how we do it there is a draft website at www.ledgerowl.com.au

Like i said, happy to consider anything that comes up :)

Target Market(s)

i'm targeting small business owners who experience a lot of stress around finacial reporting and have had bad experiences with accountants in the past.

Industry/Entity Type

Accounting

Contact Information for Business Card

Contained in the Description

Font styles to use
Serif
Sans Serif
Other font styles liked:
• See logo files attached

Colors
474747

Requirements
Must have
• My logo, slogan and contact information

```html
<!DOCTYPE html>
<html lang="en">
<head>
<meta charset="utf-8">
<title>Gus Tarrow – Business Card (Back)</title>
<link href="https://fonts.googleapis.com/css2?family=Fira+Sans:wght@400&family=Syncopate:wght@700&display=swap" rel="stylesheet">
<style>
  :root {
    --card-bg: #272e3e;
    --accent-yellow: #ffcc00;
    --name-purple: #8d3a7f;
    --contact-purple: #a9709c;
  }
  html, body {
    margin: 0;
    padding: 0;
    width: 1200px;
    height: 734px;
    overflow: hidden;
    background: var(--card-bg);
  }
  .card {
    position: relative;
    width: 1200px;
    height: 734px;
    background: var(--card-bg);
    font-family: "Fira Sans", sans-serif;
  }
  .rule {
    position: absolute;
    left: 94px;
    width: 83px;
    height: 2px;
  }
  .rule--yellow { background: var(--accent-yellow); }
  .rule--purple { background: var(--contact-purple); }

  .call-to-action {
    position: absolute;
    left: 195px;
    top: 84px;
    margin: 0;
    font-size: 43px;
    line-height: 62px;
    font-weight: 400;
    color: var(--accent-yellow);
  }
  .name {
    position: absolute;
    left: 94px;
    top: 346px;
    margin: 0;
    font-family: "Syncopate", sans-serif;
    font-weight: 700;
    font-size: 50px;
    line-height: 60px;
    letter-spacing: 1px;
    color: var(--name-purple);
    text-transform: uppercase;
  }
  .contact-row {
    position: absolute;
    left: 195px;
    height: 44px;
    display: flex;
    align-items: center;
    gap: 14px;
    color: var(--contact-purple);
    font-size: 36px;
  }
  .contact-icon {
    flex: none;
    display: block;
  }
  .website {
    position: absolute;
    left: 94px;
    top: 604px;
    font-size: 36px;
    line-height: 44px;
    color: var(--accent-yellow);
  }
</style>
</head>
<body>
  <div class="card">
    <span class="rule rule--yellow" style="top:114px"></span>
    <p class="call-to-action">Looking for a more relaxed,<br>friendly and interactive relationship<br>with your accountant?</p>

    <h1 class="name">Gus Tarrow</h1>

    <span class="rule rule--purple" style="top:446px"></span>
    <div class="contact-row" style="top:425px">
      <svg class="contact-icon" width="44" height="30" viewBox="0 0 44 30" aria-hidden="true">
        <rect x="1.5" y="1.5" width="41" height="27" fill="none" stroke="var(--contact-purple)" stroke-width="3"/>
        <path d="M2 2 L22 18 L42 2 M2 28 L17 14 M42 28 L27 14" fill="none" stroke="var(--contact-purple)" stroke-width="3"/>
      </svg>
      <span class="contact-text">gus@ledgerowl.com.au</span>
    </div>

    <span class="rule rule--purple" style="top:507px"></span>
    <div class="contact-row" style="top:486px">
      <svg class="contact-icon" width="44" height="44" viewBox="0 0 44 44" aria-hidden="true">
        <rect x="8" y="1.5" width="27" height="41" rx="4" fill="none" stroke="var(--contact-purple)" stroke-width="3"/>
        <line x1="8" y1="33" x2="35" y2="33" stroke="var(--contact-purple)" stroke-width="3"/>
        <circle cx="21.5" cy="38" r="2" fill="var(--contact-purple)"/>
      </svg>
      <span class="contact-text">1300 762 349</span>
    </div>

    <div class="website">www.ledgerowl.com.au</div>
  </div>
</body>
</html>
```